Dog care service needs business card design

Our company is Paws Harbour. We provide care for dogs while their owners are away, either through home visits or a holiday stay in the homes of carefully selected minders. Our existing website & Chatterbook cover should provide all the colour cues for our business cards - namely blues, blondes and grey. We have an existing logo (provided).

www.pawsharbourcare.example.au
www.facebook.com/pawsharbourcareau

We wish to clearly communicate our three areas of service "dog minding, home visits, dog walking".

We would like to have the files ready for upload to Printlyne (or similar) for immediate printing.

Target Market(s)

Dog owners who love their dogs like family

Industry/Entity Type

Business

Contact Information for Business Card

Paws Harbour
Ph: 0417 358 904

Font styles to use
Sans Serif

Colors
33a6d7
3176b5

Requirements
Must have
• Logo
• Telephone number
• website
• "Dog minding, home visits, dog walking"
Should not have
• any additional illustrations beyond the logo.

```html
<!DOCTYPE html>
<html lang="en">
<head>
<meta charset="utf-8">
<title>Paws Harbour – Business Cards</title>
<link rel="stylesheet" href="https://fonts.googleapis.com/css2?family=Arimo:ital,wght@0,400;0,600;1,400&display=swap">
<style>
  :root {
    --backdrop: #3a2418;
    --slate: #3d4a5c;
    --ink: #3b4556;
    --sky: #1f97d4;
    --paper: #ffffff;
    --muted: #4a4f58;
  }
  * { box-sizing: border-box; margin: 0; padding: 0; }
  html, body { width: 1200px; height: 921px; overflow: hidden; }
  body {
    background: var(--backdrop);
    font-family: "Arimo", Arial, sans-serif;
    position: relative;
  }
  .card {
    position: absolute;
    background: var(--paper);
    box-shadow: 0 6px 18px rgba(0,0,0,0.45);
    overflow: hidden;
  }
  /* Front */
  .card-front {
    left: 215px; top: 205px; width: 390px; height: 226px;
    border-top: 32px solid var(--slate);
    border-bottom: 32px solid var(--slate);
    display: flex; align-items: center; justify-content: center; gap: 18px;
  }
  .brand-mark {
    width: 56px; height: 56px; border-radius: 50%;
    background: var(--ink);
    flex: none;
  }
  .brand-name {
    font-weight: 600; font-size: 36px; line-height: 1.05;
    color: var(--ink); letter-spacing: -0.5px;
  }
  /* Back */
  .card-back {
    left: 640px; top: 398px; width: 390px; height: 220px;
    border-top: 22px solid var(--sky);
    border-bottom: 24px solid var(--sky);
    display: flex; flex-direction: column; align-items: center;
    padding-top: 10px;
  }
  .services {
    font-style: italic; font-size: 17px; color: var(--sky);
  }
  .back-mark {
    width: 68px; height: 68px; border-radius: 50%;
    background: var(--ink);
    margin: 14px 0 12px;
  }
  .phone {
    display: flex; align-items: center; gap: 6px;
    font-size: 15px; color: var(--ink);
  }
  .phone svg { width: 13px; height: 13px; flex: none; }
  .website {
    font-size: 11.5px; color: var(--muted); margin-top: 4px; letter-spacing: 0.2px;
  }
</style>
</head>
<body>
  <section class="card card-front" aria-label="Business card front">
    <span class="brand-mark" aria-hidden="true"></span>
    <h1 class="brand-name">Paws<br>Harbour</h1>
  </section>

  <section class="card card-back" aria-label="Business card back">
    <p class="services">Dog Minding, Home Visits, Dog Walking</p>
    <span class="back-mark" aria-hidden="true"></span>
    <p class="phone">
      <svg viewBox="0 0 16 16" aria-hidden="true">
        <circle cx="8" cy="8" r="7.2" fill="none" stroke="currentColor" stroke-width="1.3"/>
        <path transform="translate(2.4 2.4) scale(0.7)" d="M4.5 3.5c.5-.4 1.2-.3 1.5.2l1 1.6c.3.5.2 1.1-.3 1.4l-.6.4c.5 1 1.3 1.8 2.3 2.3l.4-.6c.3-.5.9-.6 1.4-.3l1.6 1c.5.3.6 1 .2 1.5l-.6.7c-.6.6-1.5.8-2.3.4C6.9 11 5 9.1 3.9 6.8c-.4-.8-.2-1.7.4-2.3z" fill="currentColor"/>
      </svg>
      0417 358 904
    </p>
    <p class="website">www.pawsharbourcare.example.au</p>
  </section>
</body>
</html>
```